new business card design - modern, professional, bold, B2B focus - with QR code pls

we are looking for a modern looking, colorful, business card design. some highlights:
- put space for QR code please. probably on the back but I'm open.
- biz card to be orientated VERTICAL not the traditional horizontal.
- do NOT use our full name on the card (ie: Allied Furnace Servicing Inc). Use only AFS Inc or AFS.
- use black and orange with some white. ideally black card with orange and white for the letters/logo etc. gray ok too - for outlines etc.
- we work in HEAVY industrial, so the cards should lend itself to this. our website is alfurnace.example, so you can see what we do.
- do NOT put in little smoke stack pictures / silouettes etc.
- think MODERN and INDUSTRIAL, with a techy focus.

Industry/Entity Type

heavy industrial - all of them. we perform maintenance and inspection services at heavy industrial and commercial businesses. so B2B

Contact Information for Business Card

name, title, phone numbers (cell + hardline), website, email address. of course our logo too - either on front or front and back.

Font styles to use
Other font styles liked:
• montserrat

Colors
F0912C
F2A743
F7CA91
FBE8D2
FDF5EE

Requirements
Must have
• see description
Nice to have
• see description
Should not have
• see description

```html
<!DOCTYPE html>
<html lang="en">
<head>
<meta charset="utf-8">
<title>AFS Inc — Business Card</title>
<link rel="stylesheet" href="https://fonts.googleapis.com/css2?family=Montserrat:wght@500;800&family=Oswald:wght@700&display=swap">
<style>
  :root {
    --stage: #e6e4e1;
    --card: #2a2a2c;
    --orange: #f0912c;
    --white: #ffffff;
    --pattern-light: #6b6b6e;
    --pattern-dark: #222224;
    --qr-fill: #f4f2ef;
  }
  * { box-sizing: border-box; margin: 0; padding: 0; }
  html, body { width: 1200px; height: 1200px; overflow: hidden; }
  body {
    background: var(--stage);
    display: flex; align-items: center; justify-content: center; gap: 60px;
    font-family: "Montserrat", sans-serif;
  }
  .card {
    width: 400px; height: 660px;
    background: var(--card);
    border-radius: 26px;
    position: relative;
    overflow: hidden;
    box-shadow: 0 10px 30px rgba(0,0,0,.25);
  }
  /* front */
  .card-front { display: flex; flex-direction: column; align-items: center; color: var(--white); }
  .brand-mark {
    margin-top: 110px;
    font-weight: 800; font-size: 130px; line-height: 1;
    letter-spacing: -4px;
    color: var(--orange);
  }
  .person-name {
    margin-top: 70px;
    font-family: "Oswald", sans-serif; font-weight: 700;
    font-size: 32px; line-height: 1.2; letter-spacing: 1px; text-transform: uppercase;
    color: var(--orange);
  }
  .person-title { font-size: 21px; font-weight: 500; margin-top: 2px; }
  .icon-row { display: flex; align-items: center; gap: 10px; margin-top: 16px; width: 100%; padding: 0 30px; }
  .icon-row .rule { flex: 1; height: 2px; background: var(--orange); }
  .icons { display: flex; gap: 7px; }
  .icon { width: 22px; height: 22px; background: var(--orange); border-radius: 4px; display: flex; align-items: center; justify-content: center; }
  .icon svg { width: 14px; height: 14px; }
  .contact-list { list-style: none; text-align: center; margin-top: 12px; font-size: 19px; line-height: 1.3; font-weight: 500; }
  .divider { width: 340px; height: 2px; background: var(--orange); margin: 14px 0 12px; }
  .address { text-align: center; font-size: 18px; line-height: 1.35; font-weight: 500; }
  /* back */
  .back-pattern {
    position: absolute; inset: 0;
    background: linear-gradient(210deg, var(--pattern-light) 0%, #444447 30%, var(--pattern-dark) 70%);
  }
  .qr-slot {
    position: absolute; left: 60px; bottom: 80px;
    width: 140px; height: 140px;
    background: var(--qr-fill);
    border: 6px solid var(--orange);
    border-radius: 10px;
  }
  .back-mark {
    position: absolute; right: 50px; bottom: 90px;
    font-weight: 800; font-size: 70px; line-height: 1; letter-spacing: -2px;
    color: var(--orange);
  }
</style>
</head>
<body>
  <section class="card card-front" aria-label="Card front">
    <div class="brand-mark">AFS</div>
    <h1 class="person-name">Dorian Hale</h1>
    <p class="person-title">CEO/Founder</p>
    <div class="icon-row">
      <span class="rule"></span>
      <div class="icons">
        <span class="icon"><svg viewBox="0 0 24 24" fill="none" stroke="#2a2a2c" stroke-width="2.4"><path d="M5 3h4l2 5-3 2a12 12 0 0 0 6 6l2-3 5 2v4a2 2 0 0 1-2 2A18 18 0 0 1 3 5a2 2 0 0 1 2-2z"/></svg></span>
        <span class="icon"><svg viewBox="0 0 24 24" fill="none" stroke="#2a2a2c" stroke-width="2.4"><rect x="6" y="2" width="12" height="20" rx="2"/><path d="M11 18h2"/></svg></span>
        <span class="icon"><svg viewBox="0 0 24 24" fill="none" stroke="#2a2a2c" stroke-width="2.4"><rect x="3" y="5" width="18" height="14" rx="1"/><path d="M3 6l9 7 9-7"/></svg></span>
        <span class="icon"><svg viewBox="0 0 24 24" fill="none" stroke="#2a2a2c" stroke-width="2.4"><circle cx="12" cy="12" r="9"/><path d="M3 12h18M12 3c3 3 3 15 0 18M12 3c-3 3-3 15 0 18"/></svg></span>
      </div>
      <span class="rule"></span>
    </div>
    <ul class="contact-list">
      <li>877-555-0142</li>
      <li>905-555-0187</li>
      <li>afsinc@alfurnace.example</li>
      <li>www.alfurnace.example</li>
    </ul>
    <div class="divider"></div>
    <p class="address">1420 Mill Creek Road, Unit #2.<br>Eastbrook, On X0X 0X0, Canada</p>
  </section>

  <section class="card card-back" aria-label="Card back">
    <div class="back-pattern" role="img" aria-label="Tiled brand pattern fading from grey to black"></div>
    <div class="qr-slot" role="img" aria-label="Space reserved for QR code linking to alfurnace.example"></div>
    <div class="back-mark">AFS</div>
  </section>
</body>
</html>
```